Quorvantelline.com

I need a site that I can sell dewatering equipment to the construction industry.
Ie, pipes fittings pumps and other such things needed to remove the groundwater on construction sites. Here in Florida, it’s needed almost everywhere seeing we are at sea level.
I want to be able to sell these products on the site and receive

Coded - Design and coding required

1 page

```html
<!DOCTYPE html>
<html lang="en">
<head>
<meta charset="utf-8">
<title>Quorvantelline.com — Groundwater Equipment Store</title>
<link href="https://fonts.googleapis.com/css2?family=Exo+2:ital,wght@0,400;0,500;0,600;0,700;1,600&family=Lato:wght@400;700;900&family=Michroma&family=Open+Sans:wght@400;600&display=swap" rel="stylesheet">
<style>
:root{
  --green:#0f9a1c;
  --green-dark:#0b7d14;
  --green-deep:#076310;
  --green-light:#22b232;
  --ink:#1d1d1d;
  --muted:#555;
  --card:#f3f3f3;
  --white:#fff;
  --sand-1:#c9b08a;
  --sand-2:#e6d7bd;
  --forest:#3e6a2c;
}
*{box-sizing:border-box;margin:0;padding:0}
html,body{width:1200px;height:3279px;overflow:hidden}
body{position:relative;background:var(--white);font-family:"Exo 2",sans-serif;color:var(--ink)}
.abs{position:absolute}
svg{display:block}

/* Hero */
.hero{left:0;top:0;width:1200px;height:655px;
  clip-path:polygon(0 0,100% 0,100% 590px,50% 655px,0 590px);
  background:
    linear-gradient(180deg,rgba(0,0,0,.25) 0,rgba(0,0,0,0) 22%),
    radial-gradient(ellipse 40% 30% at 70% 45%,var(--sand-2),transparent 70%),
    radial-gradient(ellipse 35% 25% at 30% 60%,#d9c4a0,transparent 70%),
    linear-gradient(180deg,#7a8f5a 0,var(--forest) 14%,var(--sand-1) 30%,#d8c29c 55%,#b79a70 80%,var(--forest) 100%);}
.logo{left:44px;top:38px;font-family:"Exo 2",sans-serif;font-weight:600;font-size:25px;color:var(--white)}
.phone-pill{left:616px;top:26px;width:162px;height:30px;border:2px solid var(--white);border-radius:8px;background:var(--green);
  color:var(--white);font-weight:600;font-size:14px;display:flex;align-items:center;justify-content:center;gap:8px}
.util{top:31px;display:flex;align-items:center;gap:6px;color:var(--white);font-size:13px;font-weight:600;text-transform:uppercase}
.nav{top:96px;display:flex;align-items:center;gap:6px;color:var(--white);font-size:14px;font-weight:600;text-transform:uppercase}
.home-btn{left:510px;top:95px;width:36px;height:28px;background:var(--green);display:flex;align-items:center;justify-content:center}
.hero-title{left:0;width:1200px;top:330px;text-align:center;font-family:Lato,sans-serif;font-weight:900;font-size:41px;color:var(--white);letter-spacing:.3px;text-shadow:0 2px 4px rgba(0,0,0,.45)}
.btn{background:var(--green);color:var(--white);font-family:Lato,sans-serif;font-weight:900;font-size:18px;letter-spacing:.5px;display:flex;align-items:center;justify-content:center;text-transform:uppercase}
.shop-now{left:492px;top:396px;width:218px;height:48px}

/* Section headings */
.section-title{font-family:Michroma,sans-serif;font-size:20px;letter-spacing:1px;color:var(--ink)}

/* Products */
.categories{left:66px;top:830px;width:277px}
.cat-rail{left:341px;top:826px;width:3px;height:410px;background:var(--green)}
.cat{position:absolute;left:0;width:277px;height:48px;background:var(--green);color:var(--white);font-weight:700;font-size:14px;
  display:flex;align-items:center;padding-left:26px}
.cat.active{background:var(--white);color:var(--ink);border:2px solid var(--green);border-right:none}
.product-img{width:236px;height:187px}
.pump-red{background:radial-gradient(ellipse 45% 40% at 50% 55%,#e0242b,#b5121a 60%,var(--white) 61%)}
.pump-blue{background:radial-gradient(ellipse 45% 40% at 50% 55%,#2f5fd0,#173b9a 60%,var(--white) 61%)}
.product-info{width:236px;height:120px;background:var(--card);box-shadow:0 4px 8px rgba(0,0,0,.15);padding:14px 16px 0}
.product-name{font-weight:500;font-size:16px;line-height:22px}
.product-foot{position:absolute;left:10px;right:10px;bottom:10px;height:38px;border-top:1px solid #ddd;display:flex;align-items:center;justify-content:space-between;padding-top:6px}
.price{display:flex;align-items:center;gap:8px;font-weight:600;font-size:16px}

/* Testimonials */
.testimonials{left:0;top:1602px;width:1200px;height:608px;
  clip-path:polygon(0 0,50% 40px,100% 0,100% 548px,50% 608px,0 548px);
  background:radial-gradient(ellipse 60% 50% at 50% 45%,var(--green-light),var(--green) 55%,var(--green-dark) 100%)}
.quote-card{width:324px;height:175px;border:2px solid var(--white);border-radius:6px;background:rgba(5,70,12,.35);color:var(--white);padding:24px 12px 0 58px;font-family:"Open Sans",sans-serif;font-size:13.5px;line-height:21px}
.quote-card::after{content:"";position:absolute;left:58px;bottom:-14px;width:24px;height:24px;background:#0e6a18;border-right:2px solid var(--white);border-bottom:2px solid var(--white);transform:rotate(45deg)}
.q-open{position:absolute;left:16px;top:12px;font-family:Lato,sans-serif;font-weight:900;font-size:54px;line-height:1}
.q-close{font-family:Lato,sans-serif;font-weight:900;font-size:30px;line-height:0;vertical-align:-8px}
.avatar{width:96px;height:96px;border-radius:50%;border:4px solid var(--white);background:radial-gradient(circle at 50% 40%,#e9d8c8,#b9a898)}
.person{font-weight:600;font-style:italic;font-size:16px;color:var(--white)}

/* About */
.about-photo{left:62px;top:2300px;width:400px;height:400px;border-radius:50%;border:14px solid #ececec;
  background:linear-gradient(180deg,#9fc3e6 0,#cfd9e4 45%,#8e8a80 60%,#e08a2a 78%,#6f6656 100%)}
.about-text{left:525px;top:2376px;width:660px;font-family:"Open Sans",sans-serif;font-size:13.5px;line-height:21.5px;color:#333}
.learn-more{left:522px;top:2520px;width:221px;height:49px}

/* Footer */
.footer{left:0;top:2787px;width:1200px;height:446px;
  clip-path:polygon(0 0,50% 40px,100% 0,100% 100%,0 100%);
  background:radial-gradient(ellipse 55% 60% at 40% 45%,var(--green-light),var(--green) 60%,var(--green-dark))}
.footer-logo{left:0;width:1200px;top:2906px;text-align:center;font-weight:600;font-size:24px;color:var(--white)}
.f-col{top:2985px;color:var(--white)}
.f-head{font-weight:700;font-size:14.5px;letter-spacing:.5px;text-transform:uppercase;margin-bottom:18px}
.f-rule{width:140px;height:1px;background:rgba(255,255,255,.4);margin:-8px 0 14px}
.f-links{list-style:none;font-weight:600;font-size:13.5px;line-height:19.5px}
.contact-row{display:flex;gap:8px;font-weight:600;font-size:13.5px;line-height:17px;margin-bottom:18px}
.social-row{display:flex;align-items:center;gap:12px;font-weight:600;font-size:14px;margin-bottom:16px}
.dot{width:20px;height:20px;border-radius:50%;background:var(--white)}
.newsletter{left:857px;top:3034px;display:flex}
.newsletter .field{width:164px;height:37px;background:var(--white);color:#222;font-size:13px;font-weight:600;display:flex;align-items:center;padding-left:10px}
.newsletter .signup{width:89px;height:37px;background:var(--green-deep);color:var(--white);font-weight:700;font-size:14px;display:flex;align-items:center;justify-content:center}
.copyright{left:0;width:1200px;top:3241px;text-align:center;font-family:"Open Sans",sans-serif;font-weight:600;font-size:11.5px;color:#222;letter-spacing:.3px}
</style>
</head>
<body>

<!-- Hero -->
<div class="hero abs" role="img" aria-label="Aerial view of an open-cut sand quarry with dewatering ponds and tree lines"></div>
<div class="logo abs">Quorvantelline.com</div>
<div class="phone-pill abs">
  <svg width="14" height="14" viewBox="0 0 24 24"><path fill="#fff" d="M6.6 10.8a15 15 0 0 0 6.6 6.6l2.2-2.2a1 1 0 0 1 1-.25 11.4 11.4 0 0 0 3.6.57 1 1 0 0 1 1 1V20a1 1 0 0 1-1 1A17 17 0 0 1 3 4a1 1 0 0 1 1-1h3.5a1 1 0 0 1 1 1c0 1.250.2 2.45.57 3.57a1 1 0 0 1-.25 1z"/></svg>
  1800.555.0199
</div>
<div class="util abs" style="left:815px">
  <svg width="12" height="12" viewBox="0 0 24 24"><circle cx="12" cy="7" r="5" fill="#fff"/><path d="M2 23c0-6 4-9 10-9s10 3 10 9z" fill="#fff"/></svg>Login
</div>
<div class="util abs" style="left:896px">
  <svg width="12" height="12" viewBox="0 0 24 24"><circle cx="12" cy="12" r="10" fill="none" stroke="#fff" stroke-width="2.5"/><path d="M12 6v6l4 3" stroke="#fff" stroke-width="2.5" fill="none"/></svg>Register
</div>
<div class="util abs" style="left:1004px">
  <svg width="14" height="13" viewBox="0 0 24 22"><path d="M1 2h4l3 12h12l3-9H7" fill="none" stroke="#fff" stroke-width="2.5"/><circle cx="10" cy="19" r="2" fill="#fff"/><circle cx="18" cy="19" r="2" fill="#fff"/></svg>Cart
</div>
<div class="util abs" style="left:1080px">
  <svg width="12" height="12" viewBox="0 0 24 24"><circle cx="10" cy="10" r="7" fill="none" stroke="#fff" stroke-width="3"/><path d="M15 15l7 7" stroke="#fff" stroke-width="3"/></svg>Search
</div>

<div class="home-btn abs">
  <svg width="18" height="16" viewBox="0 0 24 22"><path d="M12 1L1 11h3v10h6v-6h4v6h6V11h3z" fill="#fff"/></svg>
</div>
<nav>
  <div class="nav abs" style="left:579px"><svg width="14" height="12" viewBox="0 0 24 20"><path d="M2 2v14h20" fill="none" stroke="#fff" stroke-width="3"/></svg>Products</div>
  <div class="nav abs" style="left:710px"><svg width="14" height="12" viewBox="0 0 24 20"><rect x="2" y="6" width="20" height="13" fill="#fff"/><rect x="2" y="1" width="20" height="3" fill="#fff"/></svg>Shop</div>
  <div class="nav abs" style="left:800px"><svg width="14" height="12" viewBox="0 0 24 20"><path d="M2 2h20v12H9l-5 4v-4H2z" fill="none" stroke="#fff" stroke-width="2.5"/></svg>Testimonials</div>
  <div class="nav abs" style="left:962px"><svg width="14" height="12" viewBox="0 0 24 20"><rect x="2" y="2" width="20" height="16" fill="#fff"/></svg>About</div>
  <div class="nav abs" style="left:1062px"><svg width="16" height="12" viewBox="0 0 24 18"><rect x="1.5" y="1.5" width="21" height="15" fill="none" stroke="#fff" stroke-width="2.5"/><path d="M2 2l10 8 10-8" fill="none" stroke="#fff" stroke-width="2.5"/></svg>Contact</div>
</nav>

<h1 class="hero-title abs">THE LEADING SUPPLIER FOR DEWATERING INDUSTRY</h1>
<div class="btn shop-now abs">Shop Now</div>

<!-- Products -->
<h2 class="section-title abs" style="left:0;width:1200px;top:752px;text-align:center">PRODUCTS</h2>

<div class="cat-rail abs"></div>
<div class="categories abs">
  <div class="cat active" style="top:0">Well Point Pumps</div>
  <div class="cat" style="top:55px">Jet Pumps</div>
  <div class="cat" style="top:110px">Hydraulic Pumps</div>
  <div class="cat" style="top:165px">Header Pipe</div>
  <div class="cat" style="top:220px">Header Pipe Plug</div>
  <div class="cat" style="top:275px">Self Jet Dewatering</div>
  <div class="cat" style="top:330px">Accessories</div>
</div>

<!-- product row 1 -->
<div class="product-img pump-red abs" style="left:400px;top:830px" role="img" aria-label="Red well point pump unit on skid"></div>
<div class="product-img pump-blue abs" style="left:649px;top:830px" role="img" aria-label="Blue well point pump unit on skid"></div>
<div class="product-img pump-red abs" style="left:898px;top:830px" role="img" aria-label="Red well point pump unit on skid"></div>

<div class="product-info abs" style="left:400px;top:1027px"><div class="product-name">Well Point Pump<br>AB - 100</div>
  <div class="product-foot"><div class="price"><svg width="22" height="22" viewBox="0 0 24 24"><circle cx="12" cy="12" r="10.5" fill="none" stroke="#222" stroke-width="2"/><text x="12" y="17" font-size="13" font-weight="700" text-anchor="middle" fill="#222" font-family="Lato">$</text></svg>1545.00</div>
  <svg width="20" height="18" viewBox="0 0 24 22"><path d="M1 2h4l3 12h12l3-9H7" fill="#222" stroke="#222" stroke-width="2"/><circle cx="10" cy="19" r="2" fill="#222"/><circle cx="18" cy="19" r="2" fill="#222"/></svg></div></div>
<div class="product-info abs" style="left:649px;top:1027px"><div class="product-name">Well Point Pump<br>AB - 101</div>
  <div class="product-foot"><div class="price"><svg width="22" height="22" viewBox="0 0 24 24"><circle cx="12" cy="12" r="10.5" fill="none" stroke="#222" stroke-width="2"/><text x="12" y="17" font-size="13" font-weight="700" text-anchor="middle" fill="#222" font-family="Lato">$</text></svg>2485.00</div>
  <svg width="20" height="18" viewBox="0 0 24 22"><path d="M1 2h4l3 12h12l3-9H7" fill="#222" stroke="#222" stroke-width="2"/><circle cx="10" cy="19" r="2" fill="#222"/><circle cx="18" cy="19" r="2" fill="#222"/></svg></div></div>
<div class="product-info abs" style="left:898px;top:1027px"><div class="product-name">Well Point Pump<br>AB - 102</div>
  <div class="product-foot"><div class="price"><svg width="22" height="22" viewBox="0 0 24 24"><circle cx="12" cy="12" r="10.5" fill="none" stroke="#222" stroke-width="2"/><text x="12" y="17" font-size="13" font-weight="700" text-anchor="middle" fill="#222" font-family="Lato">$</text></svg>1585.00</div>
  <svg width="20" height="18" viewBox="0 0 24 22"><path d="M1 2h4l3 12h12l3-9H7" fill="#222" stroke="#222" stroke-width="2"/><circle cx="10" cy="19" r="2" fill="#222"/><circle cx="18" cy="19" r="2" fill="#222"/></svg></div></div>

<!-- product row 2 -->
<div class="product-img pump-red abs" style="left:400px;top:1187px" role="img" aria-label="Red well point pump unit on skid"></div>
<div class="product-img pump-blue abs" style="left:649px;top:1187px" role="img" aria-label="Blue well point pump unit on skid"></div>
<div class="product-img pump-red abs" style="left:898px;top:1187px" role="img" aria-label="Red well point pump unit on skid"></div>

<div class="product-info abs" style="left:400px;top:1384px"><div class="product-name">Well Point Pump<br>AB - 100</div>
  <div class="product-foot"><div class="price"><svg width="22" height="22" viewBox="0 0 24 24"><circle cx="12" cy="12" r="10.5" fill="none" stroke="#222" stroke-width="2"/><text x="12" y="17" font-size="13" font-weight="700" text-anchor="middle" fill="#222" font-family="Lato">$</text></svg>1545.00</div>
  <svg width="20" height="18" viewBox="0 0 24 22"><path d="M1 2h4l3 12h12l3-9H7" fill="#222" stroke="#222" stroke-width="2"/><circle cx="10" cy="19" r="2" fill="#222"/><circle cx="18" cy="19" r="2" fill="#222"/></svg></div></div>
<div class="product-info abs" style="left:649px;top:1384px"><div class="product-name">Well Point Pump<br>AB - 101</div>
  <div class="product-foot"><div class="price"><svg width="22" height="22" viewBox="0 0 24 24"><circle cx="12" cy="12" r="10.5" fill="none" stroke="#222" stroke-width="2"/><text x="12" y="17" font-size="13" font-weight="700" text-anchor="middle" fill="#222" font-family="Lato">$</text></svg>2485.00</div>
  <svg width="20" height="18" viewBox="0 0 24 22"><path d="M1 2h4l3 12h12l3-9H7" fill="#222" stroke="#222" stroke-width="2"/><circle cx="10" cy="19" r="2" fill="#222"/><circle cx="18" cy="19" r="2" fill="#222"/></svg></div></div>
<div class="product-info abs" style="left:898px;top:1384px"><div class="product-name">Well Point Pump<br>AB - 102</div>
  <div class="product-foot"><div class="price"><svg width="22" height="22" viewBox="0 0 24 24"><circle cx="12" cy="12" r="10.5" fill="none" stroke="#222" stroke-width="2"/><text x="12" y="17" font-size="13" font-weight="700" text-anchor="middle" fill="#222" font-family="Lato">$</text></svg>1585.00</div>
  <svg width="20" height="18" viewBox="0 0 24 22"><path d="M1 2h4l3 12h12l3-9H7" fill="#222" stroke="#222" stroke-width="2"/><circle cx="10" cy="19" r="2" fill="#222"/><circle cx="18" cy="19" r="2" fill="#222"/></svg></div></div>

<!-- Testimonials -->
<section class="testimonials abs" role="img" aria-label="Green-tinted background of large dewatering pipe"></section>
<h2 class="section-title abs" style="left:0;width:1200px;top:1758px;text-align:center;color:#fff">TESTIMONIALS</h2>

<div class="quote-card abs" style="left:87px;top:1832px"><span class="q-open">&#8221;</span>Lorem ipsum dolor sit amet, consect er adipiscing elit, sed diam nonummy nibh euismod tincidunt ut laoreet do magna aliquam erat volu. Wisi enim minim veniam. <span class="q-close">&#8221;</span></div>
<div class="avatar abs" style="left:300px;top:1960px" role="img" aria-label="Customer portrait"></div>
<div class="person abs" style="left:91px;top:2027px">Marisol Penhart</div>

<div class="quote-card abs" style="left:437px;top:1832px"><span class="q-open">&#8221;</span>Lorem ipsum dolor sit amet, consect er adipiscing elit, sed diam nonummy nibh euismod tincidunt ut laoreet do magna aliquam erat volu. Wisi enim minim veniam. <span class="q-close">&#8221;</span></div>
<div class="avatar abs" style="left:650px;top:1960px" role="img" aria-label="Customer portrait"></div>
<div class="person abs" style="left:441px;top:2027px">Odile Brackwell</div>

<div class="quote-card abs" style="left:789px;top:1832px"><span class="q-open">&#8221;</span>Lorem ipsum dolor sit amet, consect er adipiscing elit, sed diam nonummy nibh euismod tincidunt ut laoreet do magna aliquam erat volu. Wisi enim minim veniam. <span class="q-close">&#8221;</span></div>
<div class="avatar abs" style="left:1000px;top:1960px" role="img" aria-label="Customer portrait"></div>
<div class="person abs" style="left:793px;top:2027px">Teodor Vancrest</div>

<!-- About -->
<div class="about-photo abs" role="img" aria-label="Site engineers in hard hats and safety vests in front of an excavator and city skyline"></div>
<h2 class="section-title abs" style="left:525px;top:2300px;font-size:18px">ABOUT US</h2>
<p class="about-text abs">Lorem ipsum dolor sit amet, consectetur adipiscing elit, sed do eiusmod tempor incididunt ut labore et dolore magna aliqua. Ut enim ad minim veniam, quis nostrud exercitation ulla mco laboris nisi ut aliquip ex ea commodo consequat. Duis aute irure dolor in reprehender it in voluptate velit esse cillum dolore eu fugiat nulla pariatur. Excepteur sint occaecat cupi datat non proident, sunt in culpa qui officia deserunt mollit anim id est laborum.</p>
<div class="btn learn-more abs">Learn More</div>

<!-- Footer -->
<footer class="footer abs" role="img" aria-label="Green-tinted background of dewatering pipework"></footer>
<div class="footer-logo abs">Quorvantelline.com</div>

<div class="f-col abs" style="left:90px">
  <div class="f-head">Quick Links</div><div class="f-rule"></div>
  <ul class="f-links"><li>Home</li><li>Products</li><li>Shop</li><li>Testimonials</li><li>About</li><li>Contact</li></ul>
</div>
<div class="f-col abs" style="left:254px">
  <div class="f-head">Information</div><div class="f-rule"></div>
  <ul class="f-links"><li>FAQs</li><li>Terms &amp; Conditions</li><li>Shipping</li><li>Return Policy</li></ul>
</div>
<div class="f-col abs" style="left:437px">
  <div class="f-head">Contact</div><div class="f-rule"></div>
  <div class="contact-row"><svg width="18" height="18" viewBox="0 0 24 24"><circle cx="12" cy="12" r="10.5" fill="none" stroke="#fff" stroke-width="2"/><path d="M12 5a4 4 0 0 0-4 4c0 3 4 9 4 9s4-6 4-9a4 4 0 0 0-4-4z" fill="#fff"/></svg><span>Quorvantelline.com<br>48 Marlow Basin Road<br>Tampa, FL 33602</span></div>
  <div class="contact-row"><svg width="18" height="18" viewBox="0 0 24 24"><circle cx="12" cy="12" r="10.5" fill="none" stroke="#fff" stroke-width="2"/><path d="M8 7l2 0 1 3-1.5 1a7 7 0 0 0 3.5 3.5l1-1.5 3 1v2a1 1 0 0 1-1 1A9 9 0 0 1 7 8a1 1 0 0 1 1-1z" fill="#fff"/></svg><span>1800.555.0199</span></div>
  <div class="contact-row"><svg width="18" height="18" viewBox="0 0 24 24"><circle cx="12" cy="12" r="10.5" fill="none" stroke="#fff" stroke-width="2"/><rect x="6.5" y="8" width="11" height="8" fill="none" stroke="#fff" stroke-width="1.6"/><path d="M7 8.5l5 4 5-4" fill="none" stroke="#fff" stroke-width="1.6"/></svg><span>info@quorvantelline.com</span></div>
</div>
<div class="f-col abs" style="left:700px">
  <div class="f-head">Follow Us</div><div class="f-rule" style="width:110px"></div>
  <div class="social-row"><span class="dot"></span>Friendloop</div>
  <div class="social-row"><span class="dot"></span>Chirpline</div>
</div>
<div class="f-col abs" style="left:857px">
  <div class="f-head">Newsletter</div><div class="f-rule" style="width:253px"></div>
</div>
<div class="newsletter abs"><div class="field">Enter Email Address</div><div class="signup">SIGN UP</div></div>

<div class="copyright abs">COPYRIGHT © 2018 QUORVANTELLINE.COM. ALL RIGHTS RESERVED.</div>

</body>
</html>
```